K9 Orbit needs a business card designed

We need a business card designed for K9 Orbit, an expansion of K9 Systems Pty Ltd (www.k9systems.com.au)

We provide high quality professional services for the Australian space industry. Our clients include the Southern Launch Bureau and companies working in the space industry. We identify people with space related skills both locally and internationally who are then contracted by clients to create products and support space launch activities.

Colours to be used:
- Navy blue #000080
- Rocket metallic #8A7F8D
- Platinum #E5E4E2
- Black #000000
- White #FFFFFF

*Front of the card*
I have attached our K9 Orbit logo, which needs to be the main item on the card. The 'Space' text should be placed to the right of the 'K9' part rather than below, similar to the attached K9 Systems card, which this card should match.

If subtext is included, however, it should read ‘Labour Hire • Consultancy • Project Delivery’ rather than the ‘Design • Build • Test • Maintain’ of the K9 Systems card.

A black background (rather than blue background in the K9 Systems card) might be good, with a white pattern as in the K9 Systems card. If colour is used, the logo should be in its standard colours (as provided for the K9 Orbit logo).

*Back of the card*
Include a smaller K9 Orbit logo on the back.

We need the following details for K9 Orbit personnel (as a template for entry):
- Name
- Company Position
- Mobile Number
- Email
- Office Address
- Include the K9 Orbit website: www.k9orbit.com.au

Overall, we'd like to see a design that communicates the adventure of space, professional integrity, and customer service. We look forward to seeing what you can come up with.

Target Market(s)

We provide high quality professional services for the Australian space industry. Our clients include the Southern Launch Bureau and companies working in the space industry.

Contact Information for Business Card

- Name
- Company Position
- Mobile Number
- Email
- Office Address

Requirements
Must have
• See project description.

```html
<!DOCTYPE html>
<html lang="en">
<head>
<meta charset="utf-8">
<title>K9 Orbit Business Card</title>
<link href="https://fonts.googleapis.com/css2?family=Roboto:wght@400;500;700&display=swap" rel="stylesheet">
<style>
  :root {
    --navy: #272872;
    --metal: #8a7f8d;
    --white: #ffffff;
    --stage: #676566;
    --shadow: #111111;
  }
  html, body {
    margin: 0;
    padding: 0;
    width: 1200px;
    height: 801px;
    overflow: hidden;
    background: var(--stage);
    font-family: "Roboto", Arial, sans-serif;
  }
  .card {
    position: absolute;
    top: 274px;
    width: 443px;
    height: 263px;
    box-shadow: 3px 3px 2px var(--shadow);
    overflow: hidden;
  }
  .card-front { left: 153px; background: var(--white); }
  .card-back { left: 625px; background: var(--navy); }

  .wave { position: absolute; left: 0; top: 0; width: 443px; height: 263px; }

  .brand {
    position: absolute;
    display: flex;
    align-items: center;
    font-weight: 500;
    text-transform: uppercase;
    white-space: nowrap;
  }
  .brand-mark { border-radius: 50%; flex: none; }
  .card-front .brand {
    right: 20px;
    top: 54px;
    color: var(--navy);
    font-size: 24px;
    letter-spacing: 9px;
    gap: 14px;
  }
  .card-front .brand-mark { width: 22px; height: 22px; background: var(--navy); }

  .card-back .brand-block {
    position: absolute;
    left: 69px;
    top: 104px;
    width: 310px;
  }
  .card-back .brand {
    position: static;
    color: var(--white);
    font-size: 34px;
    letter-spacing: 12px;
    gap: 18px;
  }
  .card-back .brand-mark { width: 32px; height: 32px; background: var(--white); }
  .tagline {
    margin: 4px 0 0 100px;
    color: var(--white);
    font-size: 10.3px;
    white-space: nowrap;
  }

  .person {
    position: absolute;
    left: 30px;
    top: 153px;
    color: var(--white);
  }
  .person-name { margin: 0; font-size: 16.5px; font-weight: 700; line-height: 20px; }
  .person-role { margin: 0; font-size: 12.6px; line-height: 15px; }
  .contact-list {
    list-style: none;
    margin: 10px 0 0;
    padding: 0;
    font-size: 12.6px;
    line-height: 15.8px;
  }
  .contact-list li { display: flex; align-items: center; gap: 3px; }
  .contact-list svg { width: 12px; height: 12px; flex: none; }

  .address {
    position: absolute;
    right: 26px;
    top: 212px;
    margin: 0;
    text-align: right;
    color: var(--white);
    font-size: 12.6px;
    line-height: 15.8px;
    font-style: normal;
  }
</style>
</head>
<body>
  <section class="card card-front">
    <svg class="wave" viewBox="0 0 443 263" aria-hidden="true">
      <path fill="var(--metal)" d="M0,122 C30,98 55,83 85,83 C130,83 175,105 212,125 C170,106 130,92 92,94 C60,96 30,112 0,134 Z"/>
      <path fill="var(--navy)" d="M0,130 C30,108 60,96 90,96 C170,96 260,184 342,184 C385,184 420,160 443,137 L443,263 L0,263 Z"/>
    </svg>

    <div class="brand"><span class="brand-mark"></span>K9 Orbit</div>

    <div class="person">
      <h1 class="person-name">DANIEL HARPER</h1>
      <p class="person-role">Managing Director</p>
      <ul class="contact-list">
        <li>
          <svg viewBox="0 0 12 12" aria-hidden="true"><rect x="2.5" y="0.8" width="7" height="10.4" rx="1.2" fill="none" stroke="#fff" stroke-width="1.2"/><circle cx="6" cy="9.3" r="0.7" fill="#fff"/></svg>
          044-987 654 321
        </li>
        <li>
          <svg viewBox="0 0 12 12" aria-hidden="true"><rect x="0.6" y="2.2" width="10.8" height="7.6" fill="#fff"/><path d="M0.6,2.2 L6,6.6 L11.4,2.2 M0.6,9.8 L4.6,5.6 M11.4,9.8 L7.4,5.6" fill="none" stroke="#272872" stroke-width="0.9"/></svg>
          info@mailname.com
        </li>
        <li>
          <svg viewBox="0 0 12 12" aria-hidden="true"><g fill="none" stroke="#fff" stroke-width="0.9"><circle cx="6" cy="6" r="5.2"/><ellipse cx="6" cy="6" rx="2.3" ry="5.2"/><path d="M0.8,6 H11.2 M1.6,3.4 H10.4 M1.6,8.6 H10.4"/></g></svg>
          www.k9orbit.com.au
        </li>
      </ul>
    </div>

    <address class="address">178, Address line goes here<br>31870,Country Name</address>
  </section>

  <section class="card card-back">
    <div class="brand-block">
      <div class="brand"><span class="brand-mark"></span>K9 Orbit</div>
      <p class="tagline">Labour Hire • Consultancy • Project Delivery</p>
    </div>
  </section>
</body>
</html>
```